Design iOS App UI/UX for RehabGauge.com

Design UI for home screen/dashboard for my iOS/Android APP RehabGauge.
See attached screen shots and User Experience description. Also go to www.RehabGauge.com and see the website description (yes, it is still under construction, its broken and incomplete).
You are designing screen #2 #5 #6A, #6B 2&5 are very similar and 6A&6B are very similar.
To understand what you are working on, the main 8 functions of the App are:
Screen: Description:
5, 6D, 6D Get Property Info
6A, 6B, 7 Get After Repaired Value
9, 10, 11 Build a Budget
14, 14A, 15 Calculate Cost of Money
18, 19 Estimate Closing Costs
13, 13B 13A Enter Holding Costs
16, 17 Predict Cost of Sale
1, 2 Let the Dashboard drive your decision
The design aesthetic we are seeking is like the Homvara.com App, and the Nestiq App.
-Open your iOS 7 mail and launch the "new message" icon and the email template is similar to what we are looking for in UI design:
-Open your iOS 7 calendar and see transitions as you click from day to week to month for the kind of UX design input we are seeking
-We don't want special coding, but off the shelf solutions. So we want you to know what can be built with available code.
Thanks,
Carl Brinsted
P.S. Please send description of your experience and links to your work.
Target Market(s)
Our Target User #1 is a house remodel guy, 50 yrs old, skilled blue collar with some college and hands on attitude.
Our Target User #2 is a Realtor who sells these houses for the remodel Fix and Flip guy.
Our Target User #3 is a Hard Money Lender who lends money to our Fix and Flip guy. He is a small business loaning 100k to 300k to our flip guys for each project. He is lending his money, or money he has personally guaranteed with local banks or friends and family.
Our Target User #4 is a landlord looking to evaluate a buy and fix and hold property. Very similar to the User #1, but he spends time managing rental property.
Industry/Entity Type
Construction
Requirements
Must have
- Easy to see, read, clean design.
The top of screen #2 should show the Profit more clearly and compare it to the "70% ARV" scenario.
the 3,6 9 months can be buttons or shown smaller somehow.
Nice to have
- Flat design. clean and lean. look at the work of Lars Mendoza if you want to get creative.
Should not have
- flashy splashy, music label like, fashion model like, hokey, cute, silly, kitchy, country, 3-D.

```html
<!DOCTYPE html>
<html lang="en">
<head>
<meta charset="utf-8">
<title>RehabGauge – Property Dashboard</title>
<link href="https://fonts.googleapis.com/css2?family=Roboto:wght@300;400&display=swap" rel="stylesheet">
<style>
  :root{
    --page:#e9e9e9;
    --screen:#f3f3f3;
    --card:#ffffff;
    --ink:#2a2a2a;
    --muted:#9a9a9a;
    --soft:#b4b4b4;
    --rule:#d6d6d6;
    --accent:#4aa8e0;
    --accent-deep:#2b6aa6;
    --pie-light:#b7d4e8;
    --pie-mid:#5aaee0;
    --pie-dark:#4a7a9b;
    --chip:#e2e2e2;
    --tabbar:#3a3a3a;
    --sub-panel:#e8e8e8;
  }
  *{box-sizing:border-box;margin:0;padding:0}
  html,body{width:1200px;height:1014px;overflow:hidden;background:var(--page);
    font-family:"Roboto",sans-serif;font-weight:300;color:var(--ink)}
  .screen{position:absolute;top:150px;width:400px;height:702px;background:var(--screen);
    overflow:hidden;border:2px solid #2b2b2b;border-radius:3px}
  .screen--overview{left:161px}
  .screen--costs{left:686px}
  .abs{position:absolute}

  .status-bar{position:absolute;top:0;left:0;right:0;height:32px;background:var(--screen);z-index:3}
  .status-bar .signal{left:10px;top:14px}
  .status-bar .time{left:0;right:0;top:12px;text-align:center;font-size:14px;font-weight:400}
  .status-bar .battery{right:12px;top:12px}

  .nav-header{position:absolute;top:32px;left:0;right:0;height:60px;background:var(--screen);z-index:3}
  .nav-header .title{left:0;right:0;top:20px;text-align:center;font-size:24px}
  .nav-header .back{left:22px;top:22px}
  .nav-header .share{right:20px;top:16px}
  .nav-header .rule{left:14px;right:14px;bottom:0;height:1px;background:#8a8a8a}

  .photo{background:linear-gradient(180deg,#3f7fc8 0%,#7aaedc 30%,#a89b7e 55%,#5c8a3c 80%,#6a9a48 100%);
    border:4px solid #fff}
  .photo--main{left:0;top:108px;width:340px;height:256px}
  .photo--next{left:345px;top:108px;width:60px;height:256px}
  .photo-count{right:22px;top:372px;font-size:13px;font-weight:400;color:#555}

  .month-picker{left:126px;top:376px;display:flex;gap:7px}
  .month{width:44px;height:44px;border-radius:50%;background:var(--chip);color:#fff;
    font-size:28px;display:flex;align-items:center;justify-content:center}
  .month--active{background:var(--accent)}
  .months-label{left:0;right:0;text-align:center;font-size:15px;font-weight:400;color:#444}

  .summary-card{position:absolute;width:362px;height:193px;background:var(--card);box-shadow:0 1px 2px rgba(0,0,0,.08)}
  .summary-card .arv{left:54px;top:10px;font-size:21px;color:var(--accent-deep)}
  .summary-card .arv small{font-size:12px;color:var(--muted)}
  .figure{right:122px;text-align:right;line-height:1}
  .figure .value{display:block;font-size:19px;color:var(--ink)}
  .figure .label{display:block;font-size:15px;color:var(--muted);margin-top:2px}
  .specs{left:256px;top:10px;width:106px;height:173px;border-left:1px solid var(--rule)}
  .spec{position:absolute;left:0;right:0;text-align:center}
  .spec .count{font-size:20px;vertical-align:middle}
  .spec .name{display:block;font-size:13px;font-weight:400;color:#333;margin-top:1px}
  .spec-rule{position:absolute;left:18px;right:18px;height:1px;background:var(--rule)}
  .more{right:-12px;top:84px;width:24px;height:24px;border-radius:50%;background:#fff;
    box-shadow:0 0 2px rgba(0,0,0,.15)}

  .tab-bar{position:absolute;left:0;right:0;bottom:0;height:62px;background:var(--tabbar);z-index:3}
  .tab{position:absolute;top:8px;width:110px;text-align:center;color:#fff;font-size:14px;font-weight:400}
  .tab svg{display:block;margin:0 auto 4px}

  .cost-row{left:22px;right:14px;display:flex;align-items:baseline}
  .cost-row .name{flex:1}
  .cost-row .amount{text-align:right}
  .cost-row .chev{width:20px;text-align:right;color:var(--muted);font-size:16px}
  .row-main .name{font-size:21px;color:var(--ink)}
  .row-main .amount{font-size:21px;color:#777}
  .sub-panel{left:0;right:0;top:462px;height:180px;background:var(--sub-panel);
    box-shadow:inset 0 6px 6px -4px rgba(0,0,0,.12)}
  .row-sub{left:48px}
  .row-sub .name{font-size:17px;color:#7a7a7a}
  .row-sub .amount{font-size:18px;color:var(--soft)}
  .row-sub .note{font-size:13px;color:var(--muted)}
  .sub-rule{left:22px;right:22px;height:1px;background:#d2d2d2}
</style>
</head>
<body>

<!-- Overview screen -->
<section class="screen screen--overview">
  <div class="status-bar">
    <svg class="abs signal" width="44" height="8" viewBox="0 0 44 8"><g fill="#222"><circle cx="4" cy="4" r="3.5"/><circle cx="13" cy="4" r="3.5"/><circle cx="22" cy="4" r="3.5"/></g><g fill="none" stroke="#222"><circle cx="31" cy="4" r="3"/><circle cx="40" cy="4" r="3"/></g></svg>
    <div class="abs time">4:21 PM</div>
    <svg class="abs battery" width="30" height="12" viewBox="0 0 30 12"><rect x=".5" y=".5" width="26" height="11" rx="2" fill="none" stroke="#222"/><rect x="2" y="2" width="8" height="8" fill="#222"/><rect x="27.5" y="4" width="2" height="4" fill="#222"/></svg>
  </div>
  <header class="nav-header">
    <svg class="abs back" width="14" height="26" viewBox="0 0 14 26"><path d="M12 1 1 13l11 12" fill="none" stroke="#333" stroke-width="2"/></svg>
    <h1 class="abs title" style="font-weight:300;font-size:24px">418 Marlow DR</h1>
    <svg class="abs share" width="24" height="32" viewBox="0 0 24 32"><path d="M8 10H1v21h22V10h-7M12 21V1M6 7l6-6 6 6" fill="none" stroke="#333" stroke-width="1.6"/></svg>
    <div class="abs rule"></div>
  </header>

  <div class="abs photo photo--main" role="img" aria-label="Photo of the brick two-storey house with front lawn"></div>
  <div class="abs photo photo--next" role="img" aria-label="Next property photo"></div>
  <div class="abs photo-count">1 of 25</div>

  <div class="abs month-picker">
    <div class="month month--active">3</div><div class="month">6</div><div class="month">9</div>
  </div>
  <div class="abs months-label" style="top:421px">Months</div>

  <div class="summary-card" style="left:18px;top:442px">
    <div class="abs arv">70%<small> ARV</small></div>
    <svg class="abs" style="left:0;top:0" width="256" height="193" viewBox="0 0 256 193">
      <path d="M82 96 L137.7 135 A68 68 0 1 0 53.3 157.6 Z" fill="var(--pie-light)"/>
      <path d="M86 100 L42 146 A56 56 0 0 0 100 154 Z" fill="var(--pie-mid)"/>
      <path d="M86 100 L100 154 L106 128 Z" fill="var(--pie-dark)"/>
      <g stroke="#2b5f8a" stroke-width="1" fill="none">
        <path d="M103 53 H240"/><path d="M94 126 H240"/><path d="M76 143 V174 H240"/>
      </g>
      <g fill="#1f4f78"><circle cx="103" cy="53" r="2.5"/><circle cx="94" cy="126" r="2.5"/><circle cx="76" cy="143" r="2.5"/></g>
    </svg>
    <div class="abs figure" style="top:32px"><span class="value">$110,000</span><span class="label">Sale</span></div>
    <div class="abs figure" style="top:106px"><span class="value">$34,994</span><span class="label">Profit</span></div>
    <div class="abs figure" style="top:152px"><span class="value">$71,060</span><span class="label">Build</span></div>
    <div class="abs specs">
      <div class="spec" style="top:8px"><span class="count">4</span>
        <svg width="32" height="16" viewBox="0 0 32 16" style="vertical-align:middle"><rect x="2" y="6" width="28" height="6" fill="#222"/><rect x="6" y="2" width="10" height="4" rx="2" fill="#222"/><rect x="2" y="2" width="2" height="14" fill="#222"/><rect x="28" y="8" width="2" height="8" fill="#222"/></svg>
        <span class="name">Beds</span></div>
      <div class="spec-rule" style="top:64px"></div>
      <div class="spec" style="top:74px"><span class="count">2</span>
        <svg width="28" height="28" viewBox="0 0 28 28" style="vertical-align:middle"><g fill="#222"><circle cx="7" cy="3" r="2.5"/><path d="M3 7h8l2 10h-3v10H4V17H1z"/><circle cx="21" cy="3" r="2.5"/><rect x="17" y="7" width="8" height="11"/><rect x="18" y="18" width="2.5" height="9"/><rect x="21.5" y="18" width="2.5" height="9"/><rect x="13.6" y="0" width=".8" height="28"/></g></svg>
        <span class="name">Baths</span></div>
      <div class="spec-rule" style="top:122px"></div>
      <div class="spec" style="top:134px"><span class="count">1</span>
        <svg width="36" height="20" viewBox="0 0 36 20" style="vertical-align:middle"><path d="M2 10l4-8h22l5 8h1v6H2z" fill="#222"/><path d="M9 4h7v6H6zM18 4h8l3 6H18z" fill="#fff"/><circle cx="9" cy="16" r="3.5" fill="#222" stroke="#fff"/><circle cx="27" cy="16" r="3.5" fill="#222" stroke="#fff"/></svg>
        <span class="name">Garage</span></div>
    </div>
    <svg class="abs more" viewBox="0 0 24 24"><path d="M10 7l5 5-5 5" fill="none" stroke="#555" stroke-width="1.5"/></svg>
  </div>

  <nav class="tab-bar">
    <div class="tab" style="left:63px">
      <svg width="40" height="26" viewBox="0 0 40 26"><path d="M0 26 10 14l6 5 10-12 4 5L40 0v26z" fill="#fff"/></svg>Investments</div>
    <div class="tab" style="left:229px">
      <svg width="32" height="28" viewBox="0 0 32 28"><rect x="0" y="0" width="32" height="8" fill="#fff"/><rect x="2" y="10" width="28" height="18" fill="#fff"/><rect x="12" y="13" width="8" height="2" fill="#3a3a3a"/></svg>Supplies</div>
  </nav>
</section>

<!-- Cost breakdown screen -->
<section class="screen screen--costs">
  <div class="status-bar">
    <svg class="abs signal" width="44" height="8" viewBox="0 0 44 8"><g fill="#222"><circle cx="4" cy="4" r="3.5"/><circle cx="13" cy="4" r="3.5"/><circle cx="22" cy="4" r="3.5"/></g><g fill="none" stroke="#222"><circle cx="31" cy="4" r="3"/><circle cx="40" cy="4" r="3"/></g></svg>
    <div class="abs time">4:21 PM</div>
    <svg class="abs battery" width="30" height="12" viewBox="0 0 30 12"><rect x=".5" y=".5" width="26" height="11" rx="2" fill="none" stroke="#222"/><rect x="2" y="2" width="8" height="8" fill="#222"/><rect x="27.5" y="4" width="2" height="4" fill="#222"/></svg>
  </div>
  <header class="nav-header">
    <svg class="abs back" width="14" height="26" viewBox="0 0 14 26"><path d="M12 1 1 13l11 12" fill="none" stroke="#333" stroke-width="2"/></svg>
    <h1 class="abs title" style="font-weight:300;font-size:24px">418 Marlow DR</h1>
    <svg class="abs share" width="24" height="32" viewBox="0 0 24 32"><path d="M8 10H1v21h22V10h-7M12 21V1M6 7l6-6 6 6" fill="none" stroke="#333" stroke-width="1.6"/></svg>
    <div class="abs rule"></div>
  </header>

  <div class="abs month month--active" style="left:130px;top:68px"></div>
  <div class="abs month" style="left:181px;top:68px"></div>
  <div class="abs months-label" style="top:95px">Months</div>

  <div class="summary-card" style="left:19px;top:115px">
    <div class="abs arv">70%<small> ARV</small></div>
    <svg class="abs" style="left:0;top:0" width="256" height="193" viewBox="0 0 256 193">
      <path d="M82 96 L137.7 135 A68 68 0 1 0 53.3 157.6 Z" fill="var(--pie-light)"/>
      <path d="M86 100 L42 146 A56 56 0 0 0 100 154 Z" fill="var(--pie-mid)"/>
      <path d="M86 100 L100 154 L106 128 Z" fill="var(--pie-dark)"/>
      <g stroke="#2b5f8a" stroke-width="1" fill="none">
        <path d="M103 53 H240"/><path d="M94 126 H240"/><path d="M76 143 V174 H240"/>
      </g>
      <g fill="#1f4f78"><circle cx="103" cy="53" r="2.5"/><circle cx="94" cy="126" r="2.5"/><circle cx="76" cy="143" r="2.5"/></g>
    </svg>
    <div class="abs figure" style="top:32px"><span class="value">$110,000</span><span class="label">Sale</span></div>
    <div class="abs figure" style="top:106px"><span class="value">$34,994</span><span class="label">Profit</span></div>
    <div class="abs figure" style="top:152px"><span class="value">$71,060</span><span class="label">Build</span></div>
    <div class="abs specs">
      <div class="spec" style="top:8px"><span class="count">4</span>
        <svg width="32" height="16" viewBox="0 0 32 16" style="vertical-align:middle"><rect x="2" y="6" width="28" height="6" fill="#222"/><rect x="6" y="2" width="10" height="4" rx="2" fill="#222"/><rect x="2" y="2" width="2" height="14" fill="#222"/><rect x="28" y="8" width="2" height="8" fill="#222"/></svg>
        <span class="name">Beds</span></div>
      <div class="spec-rule" style="top:64px"></div>
      <div class="spec" style="top:74px"><span class="count">2</span>
        <svg width="28" height="28" viewBox="0 0 28 28" style="vertical-align:middle"><g fill="#222"><circle cx="7" cy="3" r="2.5"/><path d="M3 7h8l2 10h-3v10H4V17H1z"/><circle cx="21" cy="3" r="2.5"/><rect x="17" y="7" width="8" height="11"/><rect x="18" y="18" width="2.5" height="9"/><rect x="21.5" y="18" width="2.5" height="9"/><rect x="13.6" y="0" width=".8" height="28"/></g></svg>
        <span class="name">Baths</span></div>
      <div class="spec-rule" style="top:122px"></div>
      <div class="spec" style="top:134px"><span class="count">1</span>
        <svg width="36" height="20" viewBox="0 0 36 20" style="vertical-align:middle"><path d="M2 10l4-8h22l5 8h1v6H2z" fill="#222"/><path d="M9 4h7v6H6zM18 4h8l3 6H18z" fill="#fff"/><circle cx="9" cy="16" r="3.5" fill="#222" stroke="#fff"/><circle cx="27" cy="16" r="3.5" fill="#222" stroke="#fff"/></svg>
        <span class="name">Garage</span></div>
    </div>
    <svg class="abs more" viewBox="0 0 24 24"><path d="M10 7l5 5-5 5" fill="none" stroke="#555" stroke-width="1.5"/></svg>
  </div>

  <div class="abs cost-row" style="top:318px;left:24px;right:22px">
    <span class="name" style="font-size:21px;color:var(--soft)">Target purchase</span>
    <span class="amount" style="font-size:24px;color:var(--ink);font-weight:400">$110,000</span>
  </div>
  <div class="abs sub-rule" style="top:360px;left:24px;right:82px"></div>

  <div class="abs cost-row row-main" style="top:374px;left:27px">
    <span class="name">Remodel Budget</span><span class="amount">$71,060</span><span class="chev">›</span>
  </div>
  <div class="abs cost-row row-main" style="top:427px;left:14px">
    <span class="name"><span style="font-size:18px;color:#777;margin-right:8px">×</span>Soft Costs</span><span class="amount">$28,946</span><span class="chev">›</span>
  </div>

  <div class="abs sub-panel"></div>
  <div class="abs cost-row row-sub" style="top:474px">
    <span class="name">Cost of Money</span><span class="amount">$5,587</span><span class="chev">›</span>
  </div>
  <div class="abs cost-row row-sub" style="top:492px;left:68px;right:34px">
    <span class="name note">Cash required</span><span class="amount note">$5,000</span>
  </div>
  <div class="abs sub-rule" style="top:513px"></div>
  <div class="abs cost-row row-sub" style="top:522px">
    <span class="name">Closing cost to purchase</span><span class="amount">$1,450</span><span class="chev">›</span>
  </div>
  <div class="abs sub-rule" style="top:553px"></div>
  <div class="abs cost-row row-sub" style="top:561px">
    <span class="name">Holding Costs</span><span class="amount">$2,873</span><span class="chev">›</span>
  </div>
  <div class="abs sub-rule" style="top:591px"></div>
  <div class="abs cost-row row-sub" style="top:599px">
    <span class="name">Cost of Sale</span><span class="note" style="margin-right:10px">(7%)</span><span class="amount">$17,150</span><span class="chev">›</span>
  </div>

  <nav class="tab-bar">
    <div class="tab" style="left:63px">
      <svg width="40" height="26" viewBox="0 0 40 26"><path d="M0 26 10 14l6 5 10-12 4 5L40 0v26z" fill="#fff"/></svg>Investments</div>
    <div class="tab" style="left:229px">
      <svg width="32" height="28" viewBox="0 0 32 28"><rect x="0" y="0" width="32" height="8" fill="#fff"/><rect x="2" y="10" width="28" height="18" fill="#fff"/><rect x="12" y="13" width="8" height="2" fill="#3a3a3a"/></svg>Supplies</div>
  </nav>
</section>

</body>
</html>
```